Business Cards for Branding (Advertising) Agency

We need stylish and cool business cards.
Additional info:
1) Logo - see the attachment. You can use either the three penguins or just one penguin face (square or round) - at your discretion.
2) Text and other stuff for business card:
front side:
-Logo and company name: company name - Coastal Herons - should be in English as is in logo. This is the only exception. The rest of the text will be in Russian.
-Who we are: Брендинговое агентство
-First and last name:
-Position: Управляющий партнёр
-Address:
-Phone:
-Email:
-Website:
Note: please don't use names of information fields, such as: who we are, first and last name, position, address, phone, email and website.

3) Our suggestions on design:
-The backside of the business card can be either blank or has something on it - at your discretion.
-The business card background should be either white or grey (you can use any tone of grey).

Additional Information:
1) БРЕНДИНГОВОЕ АГЕНТСТВО
2) ул. Вересковая - these two words should be together on the same line
3) тел.: +7 (495) 381-62-09
моб.: +7 (916) 740-28-51

Reason: We would like to receive more stylish designs.

```html
<!DOCTYPE html>
<html lang="ru">
<head>
<meta charset="utf-8">
<title>Coastal Herons — визитные карточки</title>
<link rel="stylesheet" href="https://fonts.googleapis.com/css2?family=Open+Sans:wght@400;600;700;800&display=swap">
<style>
  :root {
    --bg: #5f6366;
    --card-black: #0d0d0d;
    --band-light: #e9e9e9;
    --band-mid: #c9c9c9;
    --grey-text: #8a8a8a;
    --white: #ffffff;
    --mascot-dark: #1b1b1b;
    --mascot-light: #d9d9d9;
  }
  * { box-sizing: border-box; margin: 0; padding: 0; }
  html, body { width: 1200px; height: 1023px; overflow: hidden; }
  body {
    background: var(--bg);
    font-family: "Open Sans", Arial, sans-serif;
    position: relative;
  }
  .card {
    position: absolute;
    width: 760px;
    height: 422px;
    border-radius: 18px;
    overflow: hidden;
    background: var(--card-black);
    box-shadow: 0 14px 30px rgba(0,0,0,.45);
  }
  /* Front */
  .card--front { left: 110px; top: 60px; }
  .front__band {
    position: absolute; left: 0; top: 0; width: 100%; height: 190px;
    background: linear-gradient(90deg, var(--band-light), var(--band-mid));
  }
  .front__mascot {
    position: absolute; right: 0; top: 0; width: 290px; height: 320px;
    background: radial-gradient(ellipse at 55% 60%, var(--mascot-light) 0 32%, var(--mascot-dark) 34%);
    border-bottom-left-radius: 110px;
    border: 3px solid var(--white);
    border-top: none; border-right: none;
  }
  .brand {
    position: absolute; left: 46px; top: 30px;
    color: var(--card-black); text-transform: uppercase; line-height: 1;
  }
  .brand__small {
    display: block; font-weight: 400; font-size: 22px; letter-spacing: 13px;
    color: #555;
  }
  .brand__large {
    display: block; font-weight: 600; font-size: 58px; letter-spacing: 3px; margin-top: 4px;
  }
  .front__tagline {
    position: absolute; left: 46px; top: 134px;
    font-weight: 800; font-size: 25px; color: var(--grey-text);
    text-transform: uppercase; letter-spacing: .5px;
  }
  .person { position: absolute; left: 46px; top: 200px; }
  .person__name {
    font-weight: 800; font-size: 26px; color: var(--white); text-transform: uppercase;
  }
  .person__role { font-weight: 600; font-size: 22px; color: var(--grey-text); margin-top: 0; }
  .contacts { position: absolute; left: 46px; top: 276px; list-style: none; }
  .contacts li {
    display: flex; align-items: flex-start; gap: 12px;
    color: var(--white); font-size: 17px; line-height: 1.25; margin-bottom: 7px;
  }
  .contacts svg { width: 18px; height: 18px; flex: none; margin-top: 2px; fill: var(--grey-text); }
  /* Back */
  .card--back { left: 330px; top: 540px; }
  .back__mascots {
    position: absolute; left: 70px; top: 34px; width: 250px; height: 96px;
    border-radius: 48px;
    background: linear-gradient(90deg, var(--mascot-dark), var(--mascot-light), var(--mascot-dark));
  }
  .back__brand {
    position: absolute; left: 70px; top: 148px;
    color: var(--white); text-transform: uppercase; line-height: 1;
  }
  .back__brand-small {
    display: block; font-weight: 700; font-size: 30px; letter-spacing: 16px; color: var(--band-mid);
  }
  .back__brand-large {
    display: block; font-weight: 700; font-size: 80px; letter-spacing: 4px; margin-top: 4px;
  }
  .back__tagline {
    position: absolute; left: 72px; top: 282px;
    font-weight: 800; font-size: 34px; color: var(--band-mid);
    text-transform: uppercase; letter-spacing: 2px;
  }
  .social {
    position: absolute; left: 72px; bottom: 34px;
    display: flex; align-items: center; gap: 10px;
    color: var(--white); font-size: 18px; font-weight: 600;
  }
  .social__mark { width: 22px; height: 22px; border-radius: 4px; background: var(--grey-text); }
</style>
</head>
<body>
  <section class="card card--front">
    <div class="front__band"></div>
    <div class="front__mascot" role="img" aria-label="Мультяшный талисман агентства в шапке-ушанке"></div>
    <div class="brand">
      <span class="brand__small">Coastal</span>
      <span class="brand__large">Herons</span>
    </div>
    <div class="front__tagline">Брендинговое агентство</div>
    <div class="person">
      <div class="person__name">Мария Ларионова</div>
      <div class="person__role">Управляющий партнёр</div>
    </div>
    <ul class="contacts">
      <li>
        <svg viewBox="0 0 24 24"><path d="M6.6 10.8a15 15 0 0 0 6.6 6.6l2.2-2.2c.3-.3.7-.4 1-.2 1.1.4 2.300.6 3.6.6.6 0 1 .4 1 1V20c0 .6-.4 1-1 1A17 17 0 0 1 3 4c0-.6.4-1 1-1h3.5c.6 0 1 .4 1 1 0 1.3.2 2.5.6 3.6.1.3 0 .7-.2 1z"/></svg>
        +7 (916) 740-28-51
      </li>
      <li>
        <svg viewBox="0 0 24 24"><path d="M2 5h20v14H2z M2 5l10 8 10-8" stroke="#0d0d0d" stroke-width="1.5"/></svg>
        maria@coastalherons.ru
      </li>
      <li>
        <svg viewBox="0 0 24 24"><path d="M10 14a4 4 0 0 0 6 0l3-3a4 4 0 0 0-6-6l-1 1 1.5 1.5 1-1a2 2 0 0 1 3 3l-3 3a2 2 0 0 1-3 0zM14 10a4 4 0 0 0-6 0l-3 3a4 4 0 0 0 6 6l1-1-1.500-1.5-1 1a2 2 0 0 1-3-3l3-3a2 2 0 0 1 3 0z"/></svg>
        www.coastalherons.ru
      </li>
      <li>
        <svg viewBox="0 0 24 24"><path d="M12 2a7 7 0 0 0-7 7c0 5 7 13 7 13s7-8 7-13a7 7 0 0 0-7-7zm0 9.5a2.5 2.5 0 1 1 0-5 2.5 2.5 0 0 1 0 5z"/></svg>
        <span>117218, г. Москва, ул. Вересковая,<br>д.12, стр.2</span>
      </li>
    </ul>
  </section>

  <section class="card card--back">
    <div class="back__mascots" role="img" aria-label="Три мультяшных талисмана агентства в шапках-ушанках"></div>
    <div class="back__brand">
      <span class="back__brand-small">Coastal</span>
      <span class="back__brand-large">Herons</span>
    </div>
    <div class="back__tagline">Брендинговое агентство</div>
    <div class="social">
      <span class="social__mark"></span>
      CoastalHerons
    </div>
  </section>
</body>
</html>
```